Landing page for a cyber security service provider called 'Quill Vantor'

The client is a new cyber security company in need of a website landing page at quillvantor.com.

Their visual identity is modern, playful, clean and uncluttered and represents innovation, connectivity and approachability.

The company logo is provided in black (attached) but the client is open to changing the colour to align with the new website design.

The landing page needs to contain:
- A call to action with a 'Get Started' button
-Links to blank 'How it works', 'Products', 'Pricing', 'About Us' and 'Contact Us' pages (that we'll fill out later)

Target Market(s)

Medium to large businesses who probably don't understand cyber / cyber security but need their business to be protected.

Industry/Entity Type

Cyber Security

Coding

Coded - Design and coding required

Number of Pages Required

1 page

Font styles to use
Sans Serif
Other font styles liked:
• Helvetica

Requirements
Nice to have
• Hero banner at the top of the landing page.
Should not have
• Should not look like a traditional cyber / cyber security design (eg no dark blue/ black, red/black colour combinations). Please no military styles (eg no shields, cannons, swords, guns)

```html
<!DOCTYPE html>
<html lang="en">
<head>
<meta charset="utf-8">
<title>Quill Vantor — The Future of Cyber Security</title>
<link href="https://fonts.googleapis.com/css2?family=Righteous&family=Montserrat:wght@400;500;600;700&display=swap" rel="stylesheet">
<style>
:root{
  --teal:#2cc3c0;
  --teal-dark:#1a8f9c;
  --teal-light:#dff6f6;
  --lilac:#ece8fb;
  --orange:#f5a02a;
  --gold:#f5bd2a;
  --ink:#121417;
  --text:#2b2f36;
  --muted:#5f6670;
  --white:#ffffff;
  --btn:linear-gradient(90deg,#3cd5cd,#1b8a99);
}
*{margin:0;padding:0;box-sizing:border-box}
html,body{width:1200px;height:4980px;overflow:hidden}
body{position:relative;font-family:"Montserrat",Helvetica,Arial,sans-serif;color:var(--text);background:#fff}
.abs{position:absolute}
.display{font-family:"Righteous",sans-serif;color:var(--ink);font-weight:400}
.eyebrow{font-size:13px;color:var(--orange);letter-spacing:.5px;text-transform:uppercase;font-weight:500}
.btn{position:absolute;display:flex;align-items:center;justify-content:center;border-radius:26px;background:var(--btn);color:#fff;font-weight:600;font-size:16px;text-transform:uppercase;letter-spacing:.5px;text-decoration:none}
.btn-outline{position:absolute;display:flex;align-items:center;justify-content:center;border:2px solid var(--teal);border-radius:26px;color:var(--teal);font-weight:600;font-size:16px;text-transform:uppercase;text-decoration:none;background:#fff}
.glow{position:absolute;border-radius:50%;background:radial-gradient(circle,rgba(245,189,42,.45) 0%,rgba(245,189,42,0) 70%)}

/* hero */
.hero-bg{left:560px;top:0;width:640px;height:640px;border-radius:0 0 0 320px;background:linear-gradient(135deg,#d8d0fb 0%,#aee9f0 45%,#6fdcd7 100%)}
.hero-art{left:640px;top:90px;width:500px;height:500px;border-radius:40px;background:radial-gradient(circle at 50% 45%,#ffffff 0%,#e7e4fb 45%,#8fe0e2 100%)}
.brand{left:120px;top:40px;font-family:"Righteous",sans-serif;font-size:26px;color:var(--ink);display:flex;align-items:center;gap:10px}
.brand .dot{width:14px;height:14px;border-radius:50%;background:var(--teal)}
.nav a{position:absolute;top:50px;font-size:15px;color:#3b4050;text-decoration:none}
.nav .contact{top:38px;left:937px;width:137px;height:44px;border:2px solid var(--orange);border-radius:22px;color:var(--orange);display:flex;align-items:center;justify-content:center;background:#fff}
.hero-title{left:110px;top:200px;font-size:60px;line-height:66px}
.hero-title span{color:var(--teal)}
.hero-sub{left:114px;top:350px;font-size:21px;line-height:35px;color:#2b2f36}

/* section heads */
.center{width:1200px;left:0;text-align:center}
.h2{font-size:42px;line-height:44px}
.lead{font-size:15px;line-height:23px;color:#2b2f36}

/* how it works */
.step{border-radius:22px;overflow:hidden;width:471px;height:230px}
.step.lilac{background:linear-gradient(120deg,#eeeafc,#f5f4fd)}
.step.mint{background:linear-gradient(120deg,#ddf4f4,#eefafa)}
.step h3{position:absolute;left:28px;font-size:24px;font-weight:600;color:#1c2433;letter-spacing:.5px}
.step p{position:absolute;left:28px;width:180px;font-size:13px;line-height:19px;color:#333}
.panel{position:absolute;background:#fff;border-radius:14px 0 0 14px;top:22px;bottom:0;right:0;width:220px}
.panel.left{left:0;right:auto;border-radius:0 14px 0 0;width:222px}
.tiny{font-size:8px;color:#555}
.placeholder{border-radius:10px}

/* products */
.products-bg{left:0;top:1560px;width:1200px;height:760px;background:linear-gradient(180deg,#ffffff 0%,#e6f8f8 40%,#cfeff1 100%)}
.cloud{left:-60px;top:2200px;width:1320px;height:160px;background:#fff;border-radius:50% 50% 0 0/100% 100% 0 0}
.pcard{width:214px;height:215px;background:#fff;border-radius:14px;box-shadow:8px 8px 0 var(--orange),0 6px 16px rgba(0,0,0,.06)}
.pcard .art{position:absolute;left:16px;top:14px;width:70px;height:80px;border-radius:14px;background:linear-gradient(160deg,#9ff0ea,#1d9ca6)}
.pcard h4{position:absolute;left:22px;top:130px;font-size:16px;font-weight:500;color:#1c2433}
.pcard h4 span{color:var(--orange)}
.pcard p{position:absolute;left:22px;top:156px;width:175px;font-size:13px;line-height:18px;color:#333}

/* pricing */
.plan{border-radius:18px}
.plan.basic,.plan.ent{background:linear-gradient(170deg,#ece8fb 0%,#dff5f5 100%)}
.plan.pro{background:linear-gradient(170deg,#2fc9c3,#2fa6c9);color:#fff}
.plan h5{position:absolute;left:37px;font-size:15px;font-weight:600;color:#1c2433}
.plan .desc{position:absolute;left:37px;width:235px;font-size:11.5px;line-height:15px;color:#333}
.plan .price{position:absolute;left:37px;font-size:34px;font-weight:600;color:#111}
.plan .per{position:absolute;left:37px;font-size:11.5px;color:#333}
.plan ul{position:absolute;left:37px;list-style:none}
.plan li{height:23.5px;font-size:12.5px;color:#333;display:flex;align-items:center;gap:8px}
.plan li svg{width:12px;height:12px}
.plan.pro h5,.plan.pro .price{color:#fff}
.plan.pro .desc,.plan.pro li,.plan.pro .per{color:#e4fbfb}
.toggle{left:575px;top:2555px;width:50px;height:26px;border-radius:13px;background:#d9f3f3}
.toggle::after{content:"";position:absolute;left:3px;top:3px;width:20px;height:20px;border-radius:50%;background:var(--teal)}

/* about */
.feature-icon{width:38px;height:38px;border-radius:8px;background:linear-gradient(160deg,#3cd5cd,#1b8a99)}
.feature h6{font-size:15px;font-weight:600;color:#1a6f9a;line-height:19px}

/* contact */
.contact-bg{left:0;top:3790px;width:1200px;height:1190px;background:linear-gradient(180deg,#36c3c7 0%,#3ab3cc 35%,#5c8fd3 62%,#9c86c8 82%,#e4827a 100%)}
.contact-cloud{left:80px;top:3760px;width:1040px;height:180px;background:#3ac3c6;border-radius:50% 50% 0 0/100% 100% 0 0}
.form-back{left:232px;top:4203px;width:773px;height:425px;border-radius:22px;background:var(--orange)}
.form-card{left:212px;top:4183px;width:773px;height:425px;border-radius:22px;background:#fff}
fieldset{position:absolute;border:1.5px solid #cfd3d8;border-radius:8px;padding:0 18px}
legend{font-size:14px;font-weight:600;color:#1c2433;padding:0 4px;margin-left:-4px}
fieldset .ph{font-size:13px;color:#8a9099;margin-top:4px;display:flex;justify-content:space-between;align-items:center}
fieldset .ph svg{width:13px;height:13px}

/* footer */
.foot-brand{left:126px;top:4780px;font-family:"Righteous",sans-serif;font-size:30px;color:#fff;display:flex;align-items:center;gap:10px}
.foot-brand .dot{width:16px;height:16px;border-radius:50%;background:#fff}
.social{top:4878px;width:20px;height:20px;border-radius:4px;background:#fff}
.fcol{top:4745px;border-left:2px solid #fff;padding-left:16px;color:#fff}
.fcol h6{font-size:15px;font-weight:600;margin-bottom:14px}
.fcol a,.fcol div{display:block;font-size:13px;color:#f1f4ff;text-decoration:none;height:25px}
.copy{left:0;width:1200px;top:4932px;text-align:center;color:#fff;font-size:12px}
.totop{left:1090px;top:4844px;width:50px;height:50px;border-radius:50%;background:var(--btn);border:3px solid #fff;display:flex;align-items:center;justify-content:center}
</style>
</head>
<body>

<!-- hero -->
<div class="abs hero-bg"></div>
<div class="abs hero-art" role="img" aria-label="Illustration of a laptop with fingerprint login, credit card and security badges"></div>

<header>
  <div class="abs brand"><span class="dot"></span>Quill Vantor</div>
  <nav class="nav">
    <a href="#how" style="left:468px">How it works</a>
    <a href="#products" style="left:597px">Products</a>
    <a href="#pricing" style="left:697px">Pricing</a>
    <a href="#about" style="left:782px">About Us</a>
    <a href="#contact" class="contact">Contact Us</a>
  </nav>
</header>

<div class="glow" style="left:56px;top:165px;width:70px;height:70px" role="img" aria-label="Golden sparkle decoration"></div>
<h1 class="abs display hero-title">The Future of<br><span>Cyber Security</span></h1>
<p class="abs hero-sub">Modern Solutions for Comprehensive<br>Protection and Peace of Mind</p>
<a href="#start" class="btn" style="left:114px;top:448px;width:172px;height:46px">Get Started</a>

<!-- how it works -->
<section id="how">
  <div class="abs center eyebrow" style="top:664px">How it works</div>
  <h2 class="abs center display h2" style="top:696px">How We Protect Your<br>Organization</h2>
  <p class="abs center lead" style="top:796px">At Quill Vantor, we believe in a seamless approach to cybersecurity. Our platform is designed<br>to provide you with comprehensive protection through a series of easy-to-follow steps.<br>Here’s how Quill Vantor keeps you secure</p>

  <div class="abs step lilac" style="left:116px;top:912px">
    <h3 style="top:62px">PREVENT</h3>
    <p style="top:102px">Detect vulnerabilities and block threats before they occur.</p>
    <div class="panel">
      <div class="abs tiny" style="left:16px;top:14px;font-weight:600">Statistics</div>
      <div class="abs tiny" style="left:140px;top:12px;color:#c03">● High risk</div>
      <div class="abs tiny" style="left:140px;top:24px;color:#33f">● Low risk</div>
      <svg class="abs" style="left:14px;top:40px" width="196" height="140" viewBox="0 0 196 140">
        <path d="M10 120 C40 80 55 130 80 95 S120 40 140 90 S175 10 190 20" fill="none" stroke="#d6336c" stroke-width="2"/>
        <path d="M10 110 C35 120 55 70 85 105 S125 100 145 70 S175 60 190 40" fill="none" stroke="#4c4cff" stroke-width="2"/>
        <text x="10" y="138" font-size="8" fill="#777">Jan</text><text x="60" y="138" font-size="8" fill="#777">Apr</text><text x="115" y="138" font-size="8" fill="#777">Jul</text><text x="170" y="138" font-size="8" fill="#777">Oct</text>
      </svg>
    </div>
  </div>

  <div class="abs step mint" style="left:612px;top:912px">
    <h3 style="top:62px">PROTECT</h3>
    <p style="top:102px">Safeguard your data with advanced encryption and security measures.</p>
    <div class="panel">
      <div class="abs tiny" style="left:0;width:220px;text-align:center;top:14px">Protection Effectiveness</div>
      <svg class="abs" style="left:80px;top:42px" width="60" height="60" viewBox="0 0 60 60">
        <circle cx="30" cy="30" r="24" fill="none" stroke="#f4a12a" stroke-width="8"/>
        <circle cx="30" cy="30" r="24" fill="none" stroke="#e23a3a" stroke-width="8" stroke-dasharray="40 200" transform="rotate(-90 30 30)"/>
        <circle cx="30" cy="30" r="12" fill="none" stroke="#3a7bd5" stroke-width="5"/>
      </svg>
      <div class="abs tiny" style="left:14px;top:160px;width:195px;display:flex;justify-content:space-between"><span>● Threats blocked</span><span style="color:#1a9">99.8%</span></div>
      <div class="abs tiny" style="left:14px;top:178px;width:195px;display:flex;justify-content:space-between"><span>● Encryption rate</span><span style="color:#1a9">98.1%</span></div>
      <div class="abs tiny" style="left:14px;top:196px;width:195px;display:flex;justify-content:space-between"><span>● Secure sessions</span><span style="color:#1a9">99.5%</span></div>
    </div>
  </div>

  <div class="abs step lilac" style="left:116px;top:1167px">
    <div class="panel left"><div class="abs placeholder" style="left:14px;top:18px;width:194px;height:180px;background:linear-gradient(135deg,#e8f7ff,#efe9fb)" role="img" aria-label="Automated response workflow diagram"></div></div>
    <h3 style="left:268px;top:60px">RESPOND</h3>
    <p style="left:268px;top:100px">Quickly neutralize detected threats with automated responses.</p>
  </div>

  <div class="abs step mint" style="left:612px;top:1167px">
    <div class="panel left"><div class="abs placeholder" style="left:12px;top:30px;width:198px;height:140px;background:linear-gradient(135deg,#cfe3f7,#e9f3fb)" role="img" aria-label="World map showing user locations"></div></div>
    <h3 style="left:268px;top:60px">MONITOR</h3>
    <p style="left:268px;top:100px">Ensure continuous protection with real-time monitoring and updates.</p>
  </div>

  <a href="#how" class="btn-outline" style="left:514px;top:1451px;width:170px;height:46px">Learn More</a>
</section>

<!-- products -->
<section id="products">
  <div class="abs products-bg"></div>
  <div class="abs cloud"></div>
  <div class="glow" style="left:20px;top:1650px;width:70px;height:70px" role="img" aria-label="Golden sparkle decoration"></div>
  <div class="abs eyebrow" style="left:122px;top:1708px">Products</div>
  <h2 class="abs display" style="left:116px;top:1735px;font-size:40px;line-height:44px">Explore Our<br>Cybersecurity<br>Products</h2>
  <p class="abs lead" style="left:116px;top:1893px;width:380px">Discover Quill Vantor’s innovative solutions designed to protect your digital environment with cutting-edge technology and user-friendly features.</p>
  <a href="#products" class="btn" style="left:114px;top:2001px;width:172px;height:46px">Learn More</a>

  <div class="abs pcard" style="left:603px;top:1629px"><div class="art" role="img" aria-label="Teal 3D product icon"></div><h4><span>Quill</span>Shield</h4><p>Real-time antivirus and malware protection.</p></div>
  <div class="abs pcard" style="left:844px;top:1677px"><div class="art" role="img" aria-label="Teal 3D pyramid icon"></div><h4><span>Quill</span>Guard</h4><p>Advanced firewall for network security.</p></div>
  <div class="abs pcard" style="left:603px;top:1860px"><div class="art" role="img" aria-label="Teal 3D rising bars icon"></div><h4><span>Quill</span>Secure</h4><p>Data encryption to protect your information.</p></div>
  <div class="abs pcard" style="left:844px;top:1907px"><div class="art" role="img" aria-label="Teal 3D ring icon"></div><h4><span>Quill</span>Monitor</h4><p>24/7 system monitoring with instant alerts.</p></div>
</section>

<!-- pricing -->
<section id="pricing">
  <div class="abs" style="left:565px;top:2311px;width:68px;height:68px;border-radius:50%;background:var(--btn)"></div>
  <div class="abs center eyebrow" style="top:2415px">Pricing</div>
  <h2 class="abs center display h2" style="top:2440px">Choose the Right Plan<br>for Your Needs</h2>
  <div class="abs" style="left:477px;top:2560px;font-size:13px;font-weight:600;color:#1c2433">Pay Monthly</div>
  <div class="abs toggle"></div>
  <div class="abs" style="left:636px;top:2560px;font-size:13px;font-weight:600;color:#1c2433">Pay Early</div>

  <div class="abs plan basic" style="left:116px;top:2633px;width:305px;height:423px">
    <h5 style="top:52px">Basic</h5>
    <div class="desc" style="top:78px">Essential antivirus and firewall.</div>
    <div class="price" style="top:110px">$59.99</div>
    <div class="per" style="top:154px">Per user month</div>
    <ul style="top:207px">
      <li><svg viewBox="0 0 12 12"><path d="M1 6l3 3 7-7" fill="none" stroke="#2cc3c0" stroke-width="2"/></svg>Essential antivirus</li>
      <li><svg viewBox="0 0 12 12"><path d="M1 6l3 3 7-7" fill="none" stroke="#2cc3c0" stroke-width="2"/></svg>Basic firewall protection</li>
      <li><svg viewBox="0 0 12 12"><path d="M1 6l3 3 7-7" fill="none" stroke="#2cc3c0" stroke-width="2"/></svg>Standard encryption</li>
      <li><svg viewBox="0 0 12 12"><path d="M1 6l3 3 7-7" fill="none" stroke="#2cc3c0" stroke-width="2"/></svg>Easy setup</li>
      <li><svg viewBox="0 0 12 12"><path d="M1 6l3 3 7-7" fill="none" stroke="#2cc3c0" stroke-width="2"/></svg>Affordable</li>
    </ul>
    <a href="#start" class="btn" style="left:29px;top:352px;width:245px;height:46px">Get Started</a>
  </div>

  <div class="abs plan pro" style="left:446px;top:2618px;width:306px;height:479px">
    <div class="glow" style="left:222px;top:22px;width:50px;height:50px" role="img" aria-label="Golden sparkle decoration"></div>
    <h5 style="top:34px">Professional</h5>
    <div class="desc" style="top:62px;width:180px">Advanced firewall and 24/7 monitoring.</div>
    <div class="price" style="top:125px">$89.99</div>
    <div class="per" style="top:169px">Per user month</div>
    <div class="abs" style="left:37px;top:192px;width:232px;height:1px;background:rgba(255,255,255,.6)"></div>
    <ul style="top:222px">
      <li><svg viewBox="0 0 12 12"><path d="M1 6l3 3 7-7" fill="none" stroke="#fff" stroke-width="2"/></svg>Advanced firewall</li>
      <li><svg viewBox="0 0 12 12"><path d="M1 6l3 3 7-7" fill="none" stroke="#fff" stroke-width="2"/></svg>Enhanced data encryption</li>
      <li><svg viewBox="0 0 12 12"><path d="M1 6l3 3 7-7" fill="none" stroke="#fff" stroke-width="2"/></svg>24/7 system monitoring</li>
      <li><svg viewBox="0 0 12 12"><path d="M1 6l3 3 7-7" fill="none" stroke="#fff" stroke-width="2"/></svg>Detailed threat reports</li>
      <li><svg viewBox="0 0 12 12"><path d="M1 6l3 3 7-7" fill="none" stroke="#fff" stroke-width="2"/></svg>Scalable for growth</li>
    </ul>
    <a href="#start" class="btn" style="left:31px;top:396px;width:245px;height:44px;background:#fff;color:var(--orange)">Get Started</a>
  </div>

  <div class="abs plan ent" style="left:779px;top:2633px;width:305px;height:433px">
    <h5 style="top:43px">Enterprise</h5>
    <div class="desc" style="top:70px;width:210px">Custom security and dedicated support.</div>
    <div class="price" style="top:110px">$99.99</div>
    <div class="per" style="top:154px">Per user month</div>
    <ul style="top:207px">
      <li><svg viewBox="0 0 12 12"><path d="M1 6l3 3 7-7" fill="none" stroke="#2cc3c0" stroke-width="2"/></svg>Customizable security solutions</li>
      <li><svg viewBox="0 0 12 12"><path d="M1 6l3 3 7-7" fill="none" stroke="#2cc3c0" stroke-width="2"/></svg>Advanced threat detection</li>
      <li><svg viewBox="0 0 12 12"><path d="M1 6l3 3 7-7" fill="none" stroke="#2cc3c0" stroke-width="2"/></svg>Dedicated support team</li>
      <li><svg viewBox="0 0 12 12"><path d="M1 6l3 3 7-7" fill="none" stroke="#2cc3c0" stroke-width="2"/></svg>Comprehensive coverage</li>
      <li><svg viewBox="0 0 12 12"><path d="M1 6l3 3 7-7" fill="none" stroke="#2cc3c0" stroke-width="2"/></svg>Tailored for large organizations</li>
    </ul>
    <a href="#start" class="btn" style="left:30px;top:340px;width:244px;height:45px">Get Started</a>
  </div>
</section>

<!-- about -->
<section id="about">
  <div class="abs" style="left:0;top:3250px;width:545px;height:421px;border-radius:0 18px 18px 0;background:linear-gradient(135deg,#2b2f36,#4a505a)" role="img" aria-label="Laptop displaying a user behaviour analytics dashboard"></div>
  <div class="glow" style="left:1105px;top:3225px;width:70px;height:70px" role="img" aria-label="Golden sparkle decoration"></div>
  <div class="abs eyebrow" style="left:642px;top:3252px">About us</div>
  <h2 class="abs display" style="left:636px;top:3286px;font-size:40px">Who We Are</h2>
  <p class="abs lead" style="left:636px;top:3355px;width:440px;font-size:15px">At Quill Vantor, we’re dedicated to revolutionizing cybersecurity with innovative, user-friendly solutions. Our mission is to provide effective protection that’s easy to manage, so you can focus on what matters most.</p>
  <div class="abs feature" style="left:636px;top:3480px;display:flex;gap:16px;align-items:center"><div class="feature-icon"></div><h6>Cutting-Edge<br>Technology</h6></div>
  <div class="abs feature" style="left:877px;top:3480px;display:flex;gap:16px;align-items:center"><div class="feature-icon"></div><h6>Customer-Centric<br>Approach</h6></div>
  <p class="abs lead" style="left:636px;top:3545px;width:210px">We leverage the latest advancements to keep you secure.</p>
  <p class="abs lead" style="left:877px;top:3545px;width:210px">We leverage the latest advancements to keep you secure.</p>
</section>

<!-- contact -->
<section id="contact">
  <div class="abs contact-bg"></div>
  <div class="abs contact-cloud"></div>
  <div class="abs" style="left:552px;top:3946px;width:96px;height:20px;border-radius:10px;background:var(--orange);color:#fff;font-size:11px;display:flex;align-items:center;justify-content:center;text-transform:uppercase">Contact us</div>
  <h2 class="abs center display h2" style="top:3978px;color:#fff">Let’s Protect Your<br>Organization</h2>
  <p class="abs center" style="top:4090px;color:#fff;font-size:15px;line-height:24px;font-weight:600">Use this form to ask a question and send us a comment &amp; we will<br>respond within 1 business day!</p>

  <div class="abs form-back"></div>
  <form class="abs form-card">
    <fieldset style="left:35px;top:22px;width:342px;height:50px"><legend>Full Name</legend><div class="ph"><span>Enter your name</span><svg viewBox="0 0 13 13"><circle cx="6.5" cy="4" r="2.5" fill="#8a9099"/><path d="M1.5 12c0-3 2.2-4.5 5-4.5s5 1.5 5 4.5z" fill="#8a9099"/></svg></div></fieldset>
    <fieldset style="left:398px;top:22px;width:341px;height:50px"><legend>Phono No</legend><div class="ph"><span>555 014 2286</span><svg viewBox="0 0 13 13"><path d="M3 1l2 3-1.3 1.3a7 7 0 0 0 4 4L9 8l3 2-1 2C6 12 1 7 1 2z" fill="#8a9099"/></svg></div></fieldset>
    <fieldset style="left:35px;top:97px;width:704px;height:50px"><legend>Email Address</legend><div class="ph"><span>info@example.com</span><svg viewBox="0 0 13 13"><rect x="1" y="3" width="11" height="7.5" rx="1" fill="none" stroke="#8a9099" stroke-width="1.3"/><path d="M1.5 3.5l5 4 5-4" fill="none" stroke="#8a9099" stroke-width="1.3"/></svg></div></fieldset>
    <fieldset style="left:35px;top:173px;width:704px;height:122px"><legend>Message</legend><div class="ph"><span>Type your message here</span><svg viewBox="0 0 13 13"><circle cx="6.5" cy="6.5" r="5.3" fill="none" stroke="#8a9099" stroke-width="1.3"/></svg></div></fieldset>
    <a href="#contact" class="btn" style="left:302px;top:327px;width:170px;height:44px">Submit Now</a>
  </form>
  <div class="glow" style="left:150px;top:4525px;width:160px;height:150px" role="img" aria-label="Golden sparkle decoration"></div>
</section>

<!-- footer -->
<footer>
  <div class="abs foot-brand"><span class="dot"></span>Quill Vantor</div>
  <div class="abs social" style="left:136px"></div>
  <div class="abs social" style="left:168px"></div>
  <div class="abs social" style="left:200px"></div>
  <div class="abs fcol" style="left:410px"><h6>Quick Links</h6><a href="#how">How it works</a><a href="#products">Products</a><a href="#pricing">Pricing</a><a href="#about">About Us</a></div>
  <div class="abs fcol" style="left:624px"><h6>Security</h6><a href="#products">QuillShield</a><a href="#products">QuillGuard</a><a href="#products">QuillSecure</a><a href="#products">QuillMonitor</a></div>
  <div class="abs fcol" style="left:819px;width:240px"><h6>Contact Info</h6><div style="height:40px;line-height:17px">48 Lantern Row, Brightvale,<br>Oregon 97321</div><div>555-014-2286</div><div>hello@quillvantor.com</div></div>
  <a href="#" class="abs totop"><svg width="22" height="22" viewBox="0 0 22 22"><path d="M11 19V4M4 10l7-7 7 7" fill="none" stroke="#fff" stroke-width="2.5"/></svg></a>
  <div class="abs copy">Quill Vantor© 2024 All rights reserved.</div>
</footer>

</body>
</html>
```